New professional looking flyer for company

I need our flyer updated my flyer is the Lvb flyer Have attached current flyer so you know what services need to be listed. Want it to be in mainly dark colours like black and dark grey with pops of light grey, silver or white. i have added several photos for you to choose which ones work best with your design would like The photos to be in colour for the flyer. But can have a mix of greyscale if that works for your design j have attached another companies flyers as design ideas to show what I am looking for

Target Market(s)

new clients

Industry/Entity Type

transport and earthmoving

Colors

Designer to choose colors to be used in the design.

Requirements
Nice to have
• Look professional
Should not have
• No orange or red or green

```html
<!DOCTYPE html>
<html lang="en">
<head>
<meta charset="utf-8">
<title>Lvb Pty Ltd — Our Services Flyer</title>
<link rel="stylesheet" href="https://fonts.googleapis.com/css2?family=Alfa+Slab+One&family=Open+Sans:wght@600;700&family=Graduate&display=swap">
<style>
  :root {
    --stage: #b7bcc3;
    --flyer-black: #161719;
    --flyer-charcoal: #2a2c30;
    --flyer-graphite: #3b3e43;
    --silver: #c9ccd1;
    --silver-bright: #eef0f2;
    --text-light: #e9eaec;
    --pill-blue: #2f2c8c;
  }
  * { box-sizing: border-box; margin: 0; padding: 0; }
  html, body {
    width: 1200px; height: 800px; overflow: hidden;
    background: radial-gradient(ellipse at 50% 30%, #c8ccd2 0%, var(--stage) 70%, #a9aeb5 100%);
  }
  .flyer {
    position: absolute; left: 340px; top: 50px;
    width: 520px; height: 700px; overflow: hidden;
    background: radial-gradient(ellipse at 50% 45%, var(--flyer-graphite) 0%, var(--flyer-charcoal) 45%, var(--flyer-black) 100%);
    box-shadow: 0 18px 40px rgba(0,0,0,0.35);
  }
  .flyer__frame-left, .flyer__frame-right {
    position: absolute; top: 0; height: 100%; width: 60px;
    background: linear-gradient(90deg, #0f1011, #24262a);
  }
  .flyer__frame-left { left: 0; }
  .flyer__frame-right { right: 0; transform: scaleX(-1); }
  .flyer__corner-left, .flyer__corner-right {
    position: absolute; top: 0; width: 120px; height: 150px;
  }
  .flyer__corner-left {
    left: 0; clip-path: polygon(0 0, 100% 0, 0 100%);
    background: linear-gradient(160deg, #9a9ea4 0%, #55585d 35%, rgba(30,31,34,0) 80%);
  }
  .flyer__corner-right {
    right: 0; clip-path: polygon(0 0, 100% 0, 100% 100%);
    background: linear-gradient(200deg, #a3a7ad 0%, #55585d 35%, rgba(30,31,34,0) 80%);
  }
  .flyer__band {
    position: absolute; top: 0; right: 70px; width: 210px; height: 90px;
    background: linear-gradient(180deg, #3a3d42, #222428);
    clip-path: polygon(0 0, 100% 0, 100% 100%, 70% 100%);
  }
  .brand {
    position: absolute; left: 100px; top: 52px;
    font-family: "Open Sans", sans-serif; font-weight: 700;
    font-size: 30px; color: var(--silver); letter-spacing: 1px;
    padding: 4px 0; border-top: 1px solid #777b81; border-bottom: 1px solid #777b81;
  }
  .services__title {
    position: absolute; left: 100px; top: 130px;
    font-family: "Alfa Slab One", serif; font-size: 38px; font-weight: 400;
    color: var(--silver-bright); letter-spacing: 2px;
  }
  .services__list {
    position: absolute; left: 110px; top: 188px; list-style: none;
    font-family: "Open Sans", sans-serif; font-weight: 600;
    font-size: 14px; line-height: 18px; color: var(--text-light);
  }
  .badge {
    position: absolute; left: 335px; top: 265px; width: 100px; height: 100px;
  }
  .trucks-photo {
    position: absolute; left: 40px; top: 448px; width: 450px; height: 132px;
    background: linear-gradient(90deg, #2c3a5a 0%, #5b6270 30%, #b9bcc1 48%, #4a4f58 62%, #c4c6ca 85%, #8d9096 100%);
    border-radius: 4px;
    box-shadow: 0 10px 20px rgba(0,0,0,0.5);
  }
  .flyer__floor {
    position: absolute; left: 0; bottom: 0; width: 100%; height: 140px;
    background: linear-gradient(180deg, rgba(20,21,23,0) 0%, #0c0c0d 100%);
  }
  .cta { position: absolute; left: 0; width: 100%; text-align: center; }
  .cta__note {
    top: 598px; font-family: "Graduate", serif; font-size: 12px;
    line-height: 15px; color: var(--text-light); letter-spacing: 0.5px;
  }
  .cta__call {
    top: 634px; font-family: "Open Sans", sans-serif; font-weight: 700;
    font-size: 14px; line-height: 18px; color: var(--text-light); letter-spacing: 1px;
  }
  .cta__phone {
    position: absolute; top: 658px; left: 140px; width: 240px; height: 26px;
    border-radius: 13px; background: var(--pill-blue);
    font-family: "Graduate", serif; font-size: 14px; line-height: 26px;
    text-align: center; color: var(--silver-bright); letter-spacing: 1px;
  }
</style>
</head>
<body>
  <article class="flyer">
    <div class="flyer__frame-left"></div>
    <div class="flyer__frame-right"></div>
    <div class="flyer__corner-left"></div>
    <div class="flyer__band"></div>
    <div class="flyer__corner-right"></div>

    <div class="brand">Lvb Pty Ltd</div>

    <h1 class="services__title">OUR SERVICES</h1>
    <ul class="services__list">
      <li>Over Sized Load / Hot Shot Loads</li>
      <li>Sand &amp; Metal Supply &amp; Cartage</li>
      <li>Road Building / Maintenance</li>
      <li>Heavy Vehicle Recovery</li>
      <li>Potable Water Deliveries</li>
      <li>equipment &amp; Operators</li>
      <li>Road Train Tippers</li>
      <li>Road Train Tankers</li>
      <li>Road Train Flat Tops</li>
      <li>Drop Deck Trailers</li>
      <li>Mine Site accredited</li>
      <li>Traffic Management</li>
      <li>Earthworks</li>
    </ul>

    <svg class="badge" viewBox="0 0 100 100" aria-hidden="true">
      <circle cx="50" cy="50" r="46" fill="#2b2d31" stroke="#d5d8dc" stroke-width="6"/>
    </svg>

    <div class="flyer__floor"></div>
    <div class="trucks-photo" role="img" aria-label="Photo of three road train trucks, one blue and two silver, parked side by side"></div>

    <p class="cta cta__note">we offer large range of service<br>not listed so</p>
    <p class="cta cta__call">CALL US</p>
    <p class="cta__phone">MOBILE - 235-4170-5382</p>
  </article>
</body>
</html>
```